Record Label Needs Design for CD Case, Booklet, and CD...

We are a christian record label looking to make a difference in this world.

We need 3 files -
The front and back of CD case and the actual CD graphics.

It is entitled

"Larkspan Records and Friends Summer Sampler 2014"

We will give you the artists and songs on the CD.

Please send IDEAS WE ARE OPEN TO ANYTHING!!!

you can find information on our record label at www.larkspanrecords.net or www.facebook.com/larkspanrecords

The 2 artists on the summer sampler are Ferncastle - and Paper Harbor

I have pictures of Ferncastle attached below, and pictures of paper harbor below...

ferncastlepraise.net has their logo
paper harbors logo is attached...

This is a guaranteed payout and Ive had much luck with pixel bazaar. Looking forward to another successful contest.

martin@larkspanrecords.net

Reason: We haven't had any responses yet so we extended this out a few days!

Reason: We need better designs...

Come on guys!  Send in some new designs!  I am not hard to please!  I just updated the color schemes, etc....

Target Market(s)

Christians

Industry/Entity Type

Artists

Colors
d3a5cc
ed9dc4
8768ae

Requirements
Must have
• Positivity
Nice to have
• Doves are nice
Should not have
• Crosses

```html
<!DOCTYPE html>
<html lang="en">
<head>
<meta charset="utf-8">
<title>Larkspan Records and Friends Summer Sampler 2014 – Front</title>
<link href="https://fonts.googleapis.com/css2?family=Montserrat:wght@800;900&family=Rye&family=Source+Sans+3:wght@400&display=swap" rel="stylesheet">
<style>
  :root {
    --page: #ffffff;
    --ink: #111111;
    --cream: #fcf6c4;
    --frame: #1a1a1a;
    --sun-yellow: #f7f52c;
    --sun-gold: #f5c92a;
    --sun-orange: #f47a22;
    --title-red: #c0330a;
    --label-dark: #2b2b2b;
  }
  html, body {
    margin: 0;
    padding: 0;
    width: 1200px;
    height: 1000px;
    overflow: hidden;
    background: var(--page);
  }
  .canvas {
    position: relative;
    width: 1200px;
    height: 1000px;
  }
  .side-label {
    position: absolute;
    left: 0;
    width: 1134px;
    top: 14px;
    margin: 0;
    text-align: center;
    font-family: "Source Sans 3", Arial, sans-serif;
    font-weight: 400;
    font-size: 84px;
    line-height: 1;
    color: var(--ink);
  }
  .cover {
    position: absolute;
    left: 0;
    top: 0;
  }
  .cover-label {
    font-family: "Montserrat", Arial, sans-serif;
    font-weight: 800;
    fill: var(--label-dark);
  }
  .cover-title {
    font-family: "Rye", Georgia, serif;
    fill: var(--title-red);
    stroke: var(--cream);
    stroke-width: 1.2;
    paint-order: stroke;
  }
  .cover-year {
    font-family: "Montserrat", Arial, sans-serif;
    font-weight: 900;
    fill: var(--label-dark);
  }
</style>
</head>
<body>
<main class="canvas">
  <h1 class="side-label">FRONT</h1>

  <svg class="cover" width="1200" height="1000" viewBox="0 0 1200 1000" aria-label="Larkspan Records and Friends Summer Sampler 2014 cover">
    <defs>
      <linearGradient id="sun-gradient" x1="0" y1="0" x2="1" y2="0">
        <stop offset="0" stop-color="var(--sun-yellow)"/>
        <stop offset="0.5" stop-color="var(--sun-gold)"/>
        <stop offset="1" stop-color="var(--sun-orange)"/>
      </linearGradient>
    </defs>

    <rect class="cover-ground" x="220" y="152" width="770" height="833" fill="var(--cream)"/>

    <polygon class="cover-pattern" role="img" aria-label="Pattern of overlapping yellow to orange triangles"
             points="220,152 990,152 990,680 935,650 850,695 620,695 220,600"
             fill="url(#sun-gradient)" opacity="0.85"/>

    <rect class="outer-frame" x="220.5" y="152.5" width="769" height="832" fill="none" stroke="var(--frame)" stroke-width="2"/>
    <rect class="inner-frame" x="240.5" y="172.5" width="729" height="792" fill="none" stroke="var(--frame)" stroke-width="2"/>

    <text class="cover-label" x="275" y="636" font-size="33" textLength="515" lengthAdjust="spacingAndGlyphs">LARKSPAN RECORDS &amp; FRIENDS</text>

    <text class="cover-title" x="240" y="748" font-size="118" textLength="585" lengthAdjust="spacingAndGlyphs">SUMMER</text>
    <text class="cover-title" x="318" y="898" font-size="118" textLength="647" lengthAdjust="spacingAndGlyphs">SAMPLER</text>

    <text class="cover-year" x="802" y="962" font-size="66" textLength="150" lengthAdjust="spacingAndGlyphs" transform="rotate(-8 877 940)">2014</text>
  </svg>
</main>
</body>
</html>
```